Create a flyer for our party getaway to Ibiza.

'The Crimson Ibiza Escape'

Friday 14th July - Monday 17th July

DJ Morvek & DJ Tundral brings together a jam-packed weekend schedule full of the best urban parties in Ibiza.

What's included?

4 Nights Of Entertainment
6 Parties In Total
1 Boat Party
1 Pool Party
2 Superclub Parties
1 Indoor Water Party
Bottomless Drinks (Boat Party Only)
An unbelievable experience
1 unbeatable price.

All this for 140€ (you save 50€ when you book with us)

Tickets avaialble from Ticketlane & Gribolo

Target Market(s)

holiday goers

Industry/Entity Type

party, events, club, hip hop

Requirements
Must have
• good vibes
Nice to have
• nice catchy looking title

```html
<!DOCTYPE html>
<html lang="en">
<head>
<meta charset="utf-8">
<title>The Crimson Ibiza Escape</title>
<link rel="stylesheet" href="https://fonts.googleapis.com/css2?family=Anton&family=Oswald:wght@300;400;600&family=Poppins:wght@400;600&family=Sacramento&family=Syncopate:wght@700&display=swap">
<style>
  :root {
    --night: #0c0d2a;
    --violet: #4a1ca8;
    --purple: #8a2be2;
    --magenta: #f0189a;
    --pink: #ff2aa6;
    --gold: #f7b21b;
    --amber: #f39a0f;
    --white: #ffffff;
    --ticket-orange: #f26b1d;
  }
  * { box-sizing: border-box; margin: 0; padding: 0; }
  html, body { width: 750px; height: 1200px; overflow: hidden; background: #ffffff; }
  .flyer {
    position: relative; width: 750px; height: 1200px; overflow: hidden;
    background: var(--night); color: var(--white);
    font-family: "Poppins", sans-serif;
  }
  .club-backdrop {
    position: absolute; inset: 0;
    background:
      radial-gradient(ellipse 60% 45% at 0% 30%, rgba(138,43,226,.75), transparent 70%),
      radial-gradient(ellipse 55% 40% at 100% 25%, rgba(106,40,220,.7), transparent 70%),
      radial-gradient(ellipse 70% 30% at 50% 0%, rgba(60,70,130,.6), transparent 70%),
      linear-gradient(180deg, #1b1a4a 0%, #0e0f2e 55%, #0b0c26 100%);
  }
  .smoke {
    position: absolute; left: 0; right: 0; bottom: 0; height: 260px;
    background:
      radial-gradient(ellipse 40% 60% at 15% 100%, rgba(138,43,226,.8), transparent 70%),
      radial-gradient(ellipse 45% 55% at 75% 100%, rgba(120,40,210,.7), transparent 70%),
      linear-gradient(0deg, rgba(90,30,180,.6), transparent);
  }
  .title-top {
    position: absolute; top: 92px; left: 0; width: 750px; text-align: center;
    font-family: "Syncopate", sans-serif; font-weight: 700; font-size: 42px;
    letter-spacing: 9px; line-height: 1;
  }
  .title-main { position: absolute; top: 150px; left: 0; width: 750px; height: 260px; }
  .title-echo { position: absolute; top: 370px; left: 0; width: 750px; height: 260px; opacity: .18; }
  .dj-photo {
    position: absolute; left: 150px; top: 290px; width: 410px; height: 405px;
    background: radial-gradient(ellipse 70% 80% at 50% 40%, rgba(190,170,200,.55), rgba(120,90,160,.35) 55%, transparent 80%);
    border-radius: 40% 40% 10% 10%;
  }
  .title-script {
    position: absolute; top: 470px; left: 0; width: 750px; text-align: center;
    font-family: "Sacramento", cursive; font-size: 190px; line-height: 1;
    color: #fff4fb; transform: rotate(-6deg);
    text-shadow: 0 0 6px var(--pink), 0 0 18px var(--magenta), 0 0 34px var(--magenta);
  }
  .headliners {
    position: absolute; top: 693px; left: 0; width: 750px; text-align: center;
    font-family: "Oswald", sans-serif; font-weight: 600; font-size: 46px;
    letter-spacing: 5px; color: var(--gold); line-height: 1;
  }
  .headliners .amp { font-weight: 300; color: var(--white); }
  .tagline {
    position: absolute; top: 754px; left: 0; width: 750px; text-align: center;
    font-size: 15px; line-height: 19px; text-transform: uppercase;
  }
  .dates { position: absolute; left: 74px; top: 852px; font-family: "Oswald", sans-serif; text-transform: uppercase; line-height: 1; }
  .dates .day { font-weight: 300; font-size: 24px; display: block; }
  .dates .date { font-weight: 600; font-size: 44px; color: var(--pink); display: block; margin: 2px 0 16px; letter-spacing: -1px; }
  .dates .to { font-size: 20px; }
  .included { position: absolute; left: 270px; top: 842px; font-family: "Oswald", sans-serif; text-transform: uppercase; }
  .included h2 { font-size: 32px; line-height: 1; color: var(--gold); font-weight: 300; margin-bottom: 14px; letter-spacing: -.5px; }
  .included h2 strong { font-weight: 600; }
  .included .cols { display: flex; gap: 18px; }
  .included ul { list-style: none; }
  .included li { font-weight: 300; font-size: 15px; line-height: 24.5px; display: flex; align-items: center; gap: 5px; white-space: nowrap; }
  .included li svg { width: 13px; height: 13px; flex: none; }
  .offer { position: absolute; left: 77px; top: 1056px; display: flex; align-items: center; }
  .price-badge {
    width: 167px; height: 71px; border-radius: 8px; display: flex; align-items: center; gap: 6px; padding-left: 12px;
    background: linear-gradient(135deg, var(--gold), var(--amber));
  }
  .price-badge .lead { font-family: "Poppins", sans-serif; font-weight: 600; font-size: 15px; line-height: 15px; color: #2a1a6a; text-align: center; }
  .price-badge .amount { font-family: "Oswald", sans-serif; font-weight: 600; font-size: 58px; line-height: 1; letter-spacing: -2px; }
  .saving { margin-left: 12px; font-size: 14px; line-height: 18px; text-transform: uppercase; }
  .divider { position: absolute; left: 395px; top: 1060px; width: 1px; height: 64px; background: rgba(255,255,255,.8); }
  .tickets { position: absolute; left: 415px; top: 1058px; font-family: "Oswald", sans-serif; }
  .tickets h3 { font-weight: 400; font-size: 22px; letter-spacing: 4px; line-height: 1; text-transform: uppercase; }
  .vendors { display: flex; align-items: center; gap: 26px; margin-top: 14px; }
  .vendor { display: flex; align-items: center; gap: 6px; font-family: "Poppins", sans-serif; font-weight: 600; font-size: 19px; color: var(--white); line-height: 1; }
  .vendor .mark { width: 12px; height: 12px; background: var(--ticket-orange); }
</style>
</head>
<body>
<main class="flyer">
  <div class="club-backdrop" role="img" aria-label="Dim nightclub interior with purple stage lights"></div>
  <div class="smoke" role="img" aria-label="Purple haze along the bottom edge"></div>

  <h1>
    <span class="title-top">THE CRIMSON</span>
    <svg class="title-main" viewBox="0 0 750 260" aria-hidden="true">
      <defs>
        <linearGradient id="ibizaFill" x1="0" y1="0" x2="0.3" y2="1">
          <stop offset="0" stop-color="#9a3cf0"/>
          <stop offset="0.6" stop-color="#e01aa8"/>
          <stop offset="1" stop-color="#ff1493"/>
        </linearGradient>
      </defs>
      <text x="106" y="240" textLength="536" lengthAdjust="spacingAndGlyphs" font-family="Anton, sans-serif" font-size="300" fill="url(#ibizaFill)">IBIZA</text>
    </svg>
    <span class="title-script">Escape</span>
  </h1>
  <svg class="title-echo" viewBox="0 0 750 260" aria-hidden="true">
    <text x="130" y="240" textLength="490" lengthAdjust="spacingAndGlyphs" font-family="Anton, sans-serif" font-size="280" fill="none" stroke="#ff2aa6" stroke-width="2">IBIZA</text>
  </svg>
  <div class="dj-photo" role="img" aria-label="Photo of the two headlining DJs posing in white t-shirts"></div>
  <h1 class="title-script" style="pointer-events:none" aria-hidden="true">Escape</h1>

  <p class="headliners">DJ MORVEK <span class="amp">&amp;</span> DJ TUNDRAL</p>
  <p class="tagline">Brings together a jam-packed weekend schedule full of<br>the best urban parties in Ibiza</p>

  <div class="dates">
    <span class="day">Friday</span>
    <span class="date">14th July <span class="to">to</span></span>
    <span class="day">Monday</span>
    <span class="date">17th July</span>
  </div>

  <section class="included">
    <h2>What's <strong>Included?</strong></h2>
    <div class="cols">
      <ul>
        <li><svg viewBox="0 0 14 14"><circle cx="7" cy="7" r="6" fill="none" stroke="#f7b21b" stroke-width="1.4"/><path d="M4 7.2l2.2 2.2L10.5 5" fill="none" stroke="#f7b21b" stroke-width="1.6"/></svg>4 Nights of Entertainment</li>
        <li><svg viewBox="0 0 14 14"><circle cx="7" cy="7" r="6" fill="none" stroke="#f7b21b" stroke-width="1.4"/><path d="M4 7.2l2.2 2.2L10.5 5" fill="none" stroke="#f7b21b" stroke-width="1.6"/></svg>6 Parties in Total</li>
        <li><svg viewBox="0 0 14 14"><circle cx="7" cy="7" r="6" fill="none" stroke="#f7b21b" stroke-width="1.4"/><path d="M4 7.2l2.2 2.2L10.5 5" fill="none" stroke="#f7b21b" stroke-width="1.6"/></svg>1 Boat Party</li>
        <li><svg viewBox="0 0 14 14"><circle cx="7" cy="7" r="6" fill="none" stroke="#f7b21b" stroke-width="1.4"/><path d="M4 7.2l2.2 2.2L10.5 5" fill="none" stroke="#f7b21b" stroke-width="1.6"/></svg>1 Pool Party</li>
        <li><svg viewBox="0 0 14 14"><circle cx="7" cy="7" r="6" fill="none" stroke="#f7b21b" stroke-width="1.4"/><path d="M4 7.2l2.2 2.2L10.5 5" fill="none" stroke="#f7b21b" stroke-width="1.6"/></svg>2 Superclub Parties</li>
      </ul>
      <ul>
        <li><svg viewBox="0 0 14 14"><circle cx="7" cy="7" r="6" fill="none" stroke="#f7b21b" stroke-width="1.4"/><path d="M4 7.2l2.2 2.2L10.5 5" fill="none" stroke="#f7b21b" stroke-width="1.6"/></svg>1 Indoor Water Party</li>
        <li><svg viewBox="0 0 14 14"><circle cx="7" cy="7" r="6" fill="none" stroke="#f7b21b" stroke-width="1.4"/><path d="M4 7.2l2.2 2.2L10.5 5" fill="none" stroke="#f7b21b" stroke-width="1.6"/></svg>Bottomless Drinks (Boat Party Only)</li>
        <li><svg viewBox="0 0 14 14"><circle cx="7" cy="7" r="6" fill="none" stroke="#f7b21b" stroke-width="1.4"/><path d="M4 7.2l2.2 2.2L10.5 5" fill="none" stroke="#f7b21b" stroke-width="1.6"/></svg>An Unbelievable Experience</li>
        <li><svg viewBox="0 0 14 14"><circle cx="7" cy="7" r="6" fill="none" stroke="#f7b21b" stroke-width="1.4"/><path d="M4 7.2l2.2 2.2L10.5 5" fill="none" stroke="#f7b21b" stroke-width="1.6"/></svg>1 Unbeatable Price.</li>
      </ul>
    </div>
  </section>

  <div class="offer">
    <div class="price-badge">
      <span class="lead">ALL<br>THIS<br>FOR</span>
      <span class="amount">140€</span>
    </div>
    <p class="saving">You save 50€<br>when you book<br>with us</p>
  </div>
  <div class="divider"></div>
  <div class="tickets">
    <h3>Tickets available from</h3>
    <div class="vendors">
      <span class="vendor"><span class="mark"></span>Ticketlane</span>
      <span class="vendor">Gribolo</span>
    </div>
  </div>
</main>
</body>
</html>
```